Brixel Information Technology Solutions
We are an Information Technology Company. We provide computer services to commercial companies. We would like a new card full color front and back with bleeding edge.
We have a logo that you can use or if you want to come up with a new logo that is fine too.
Our colors are mostly Maroon and black but be creative.
Sample Information
Grant P Oswick
4818 W Saguaro Ridge Drive
Suite 410
Phoenix, AZ 85016
O: 602.555.0143
C: 602.555.0178
24/7: 888.555.0162
goswick@brixelit.com
www.brixelit.com
Target Market(s)
Business of all sizes
Industry/Entity Type
Computer
Requirements
Must have
- Bleeding edge
full color on both sides

```html
<!DOCTYPE html>
<html lang="en">
<head>
<meta charset="utf-8">
<title>Brixel Business Card</title>
<link href="https://fonts.googleapis.com/css2?family=Arimo:wght@400;700&family=Tinos&display=swap" rel="stylesheet">
<style>
  :root {
    --stage: #2a2a2a;
    --card-dark: #111111;
    --card-dark-deep: #070707;
    --card-light: #ffffff;
    --card-light-tint: #f1f1f1;
    --ink: #000000;
    --ink-soft: #1c1c1c;
    --grey: #7b7b7b;
    --grey-light: #8e8e8e;
    --accent: #c71f2d;
  }
  * { margin: 0; padding: 0; box-sizing: border-box; }
  html, body {
    width: 1200px; height: 898px; overflow: hidden;
    background: var(--stage);
    font-family: "Arimo", Arial, sans-serif;
  }
  .stage { position: relative; width: 1200px; height: 898px; }
  .card { position: absolute; overflow: hidden; }
  .card-front { left: 53px; top: 39px; width: 683px; height: 397px; background: var(--card-dark); }
  .card-back { left: 394px; top: 470px; width: 677px; height: 393px; background: var(--card-light); }
  .texture { position: absolute; inset: 0; }
  .card-front .texture { background: radial-gradient(ellipse at 40% 45%, var(--card-dark) 0%, var(--card-dark-deep) 100%); }
  .card-back .texture { background: linear-gradient(180deg, var(--card-light-tint) 0%, var(--card-light) 100%); }

  .wordmark {
    position: absolute; display: flex; align-items: center; gap: 12px;
    font-family: "Arimo", Arial, sans-serif; font-weight: 400;
    font-size: 66px; line-height: 1; letter-spacing: -1px;
  }
  .wordmark .mark-square { width: 16px; height: 16px; background: var(--accent); }
  .card-front .wordmark { left: 188px; top: 162px; color: var(--grey); }
  .card-back .wordmark { left: 21px; top: 135px; color: var(--ink); }

  .tagline {
    position: absolute; font-family: "Tinos", "Times New Roman", serif;
    font-size: 15px; line-height: 1;
  }
  .card-front .tagline { left: 242px; top: 229px; color: var(--grey); }
  .card-back .tagline { left: 74px; top: 202px; color: var(--ink-soft); }

  .web {
    position: absolute; font-weight: 700; line-height: 1;
  }
  .card-front .web { right: 18px; top: 338px; font-size: 23px; color: var(--grey-light); }
  .card-back .web { left: 47px; top: 354px; font-size: 24px; color: var(--ink); }

  .contact {
    position: absolute; left: 320px; width: 342px; top: 0;
    text-align: center; color: var(--ink); font-weight: 700;
  }
  .contact .name { position: absolute; left: 0; right: 0; top: 87px; font-size: 19px; }
  .contact .line { position: absolute; left: 0; right: 0; font-size: 15px; }
  .contact .office { top: 141px; }
  .contact .cell { top: 188px; }
  .contact .support { top: 235px; }
  .contact .email { top: 282px; }
  .address {
    position: absolute; left: 342px; top: 362px;
    font-size: 12.5px; font-weight: 700; color: var(--ink);
  }
</style>
</head>
<body>
<main class="stage">
  <section class="card card-front">
    <div class="texture" role="img" aria-label="Faint field of binary digits across the dark card"></div>
    <div class="wordmark"><span class="mark-square"></span>Brixel</div>
    <p class="tagline">Information Technology Solutions</p>
    <p class="web">www.brixelit.com</p>
  </section>

  <section class="card card-back">
    <div class="texture" role="img" aria-label="Faint field of grey binary digits across the white card"></div>
    <div class="wordmark"><span class="mark-square"></span>Brixel</div>
    <p class="tagline">Information Technology Solutions</p>
    <div class="contact">
      <p class="name">Grant P Oswick</p>
      <p class="line office">O: 602.555.0143</p>
      <p class="line cell">C: 602.555.0178</p>
      <p class="line support">24/7: 888.555.0162</p>
      <p class="line email">Email: goswick@brixelit.com</p>
    </div>
    <p class="web">www.brixelit.com</p>
    <p class="address">4818 W Saguaro Ridge Drive Suite 410 Phoenix, AZ 85016</p>
  </section>
</main>
</body>
</html>
```